Handy man Company business card

need branded business card for my new company, this design will transfer to car wrap design what winner will be asked to design

I will need original file so I can edit it in the end.

Also like to have some inspirational quote like "ONE CALL WE DO IT ALL"
"We do it right" can be added to logo side

Like to try to see large 1 800 000 0000 number on front with large logo

Size bigger then standard business card

I like to integrate LAS VEGAS sign to one of sides

Target Market(s)

Handy man services, Home renovation and remodeling

Industry/Entity Type

Handyman

Contact Information for Business Card

Tool Baron LLC.
Name: BORIS LENKOVA
Phone "Temporary": 000 000 0000
Adress: 2715 Fenmore Ct, Las Vegas NV 89147
Website: www.toolbaron.vegas
Email: info@toolbaron.vegas

Requirements
Must have
• Two side
• side n1: LOGO
• side n2: INFO
Nice to have
• Like to have some interesting idea for client to remember!
• With logo added to both side at different stile
Should not have
• Standard design,

```html
<!DOCTYPE html>
<html lang="en">
<head>
<meta charset="utf-8">
<title>Tool Baron – Business Card</title>
<link rel="stylesheet" href="https://fonts.googleapis.com/css2?family=Montserrat:wght@400;500;600;700;800&display=swap">
<style>
  :root {
    --stage: #2b2b2d;
    --card-yellow: #fdbe1a;
    --card-white: #ffffff;
    --sign-orange: #f0a21e;
    --bulb-navy: #1d2a3a;
    --ink-navy: #1e3140;
    --ink-black: #1a1a1a;
    --phone-red: #e5202b;
    --accent-orange: #f2a324;
    --text-grey: #3c4650;
    --divider: #c9ccd0;
    --mascot-a: #f5b52c;
    --mascot-b: #6b8fb0;
  }
  * { box-sizing: border-box; margin: 0; padding: 0; }
  html, body { width: 1200px; height: 1000px; overflow: hidden; }
  body {
    background: var(--stage);
    font-family: "Montserrat", Arial, sans-serif;
    position: relative;
  }
  .card {
    position: absolute;
    width: 640px;
    height: 370px;
    border-radius: 22px;
    overflow: hidden;
    box-shadow: 0 14px 30px rgba(0,0,0,.45);
  }
  .card--front { left: 280px; top: 90px; background: var(--card-yellow); }
  .card--back  { left: 280px; top: 540px; background: var(--card-white); }

  .sign { position: absolute; inset: 0; }

  .front-brand {
    position: absolute;
    left: 0; right: 0; top: 104px;
    display: flex; align-items: center; justify-content: center; gap: 14px;
  }
  .mascot {
    background: linear-gradient(160deg, var(--mascot-a), var(--mascot-b));
    border-radius: 10px;
  }
  .front-brand .mascot { width: 50px; height: 72px; }
  .brand-name {
    font-weight: 700;
    color: var(--ink-navy);
    letter-spacing: .5px;
  }
  .front-brand .brand-name { font-size: 40px; }

  .front-phone {
    position: absolute;
    left: 0; right: 0; top: 184px;
    text-align: center;
    font-size: 50px; font-weight: 800;
    line-height: 60px;
    color: var(--phone-red);
    letter-spacing: 1px;
  }
  .front-tagline {
    position: absolute;
    left: 0; right: 0; top: 250px;
    text-align: center;
    font-size: 23px; font-weight: 700;
    line-height: 30px;
    color: var(--ink-black);
    letter-spacing: 2px;
  }

  .back-brand {
    position: absolute;
    left: 50px; top: 150px;
    display: flex; align-items: center; gap: 12px;
  }
  .back-brand .mascot { width: 44px; height: 66px; }
  .back-brand .brand-name { font-size: 32px; line-height: 1.05; }
  .brand-tagline {
    display: block;
    font-size: 15px; font-weight: 500;
    color: var(--ink-navy);
    letter-spacing: 4px;
    margin-top: 4px;
  }
  .divider {
    position: absolute;
    left: 330px; top: 110px;
    width: 1px; height: 150px;
    background: var(--divider);
    transform: rotate(-14deg);
  }
  .contact {
    position: absolute;
    left: 370px; top: 112px;
    color: var(--text-grey);
    font-size: 15px; line-height: 1.45;
  }
  .contact-name {
    font-size: 24px; font-weight: 600;
    color: var(--accent-orange);
    letter-spacing: 1px;
    margin-bottom: 6px;
  }
  .contact-row { display: flex; align-items: center; gap: 8px; }
  .contact-row svg { width: 12px; height: 12px; flex: none; }
  .contact-address { margin-bottom: 2px; }
</style>
</head>
<body>

  <section class="card card--front" aria-label="Card front">
    <svg class="sign" viewBox="0 0 640 370" aria-hidden="true">
      <polygon points="18,200 110,80 540,62 622,160 540,310 110,328"
               fill="var(--sign-orange)"/>
      <polygon points="42,200 122,96 530,78 600,160 526,294 122,312"
               fill="#ffffff"/>
      <polygon points="18,200 110,80 540,62 622,160 540,310 110,328"
               fill="none" stroke="var(--bulb-navy)" stroke-width="6"
               stroke-linecap="round" stroke-dasharray="0 11"/>
    </svg>
    <div class="front-brand">
      <div class="mascot" role="img" aria-label="Cartoon handyman mascot in cap and overalls"></div>
      <span class="brand-name">Tool Baron</span>
    </div>
    <div class="front-phone">1 800 000 0000</div>
    <div class="front-tagline">ONE CALL WE DO IT ALL</div>
  </section>

  <section class="card card--back" aria-label="Card back">
    <div class="back-brand">
      <div class="mascot" role="img" aria-label="Cartoon handyman mascot in cap and overalls"></div>
      <div>
        <span class="brand-name">Tool Baron</span>
        <span class="brand-tagline">We do it right</span>
      </div>
    </div>
    <div class="divider"></div>
    <div class="contact">
      <div class="contact-name">BORIS LENKOVA</div>
      <div class="contact-address">2715 Fenmore Ct<br>Las Vegas NV 89147</div>
      <div class="contact-row">
        <svg viewBox="0 0 12 12" aria-hidden="true"><path d="M2 1l2 0 1 3-1.5 1a6 6 0 0 0 3 3L7.5 6.5l3 1 0 2-1.5 1.5C5 10.5 1.5 7 1 2.5z" fill="var(--accent-orange)"/></svg>
        <span>1 800 000 0000</span>
      </div>
      <div class="contact-row">
        <svg viewBox="0 0 12 12" aria-hidden="true"><rect x="1" y="2.5" width="10" height="7" rx="1" fill="none" stroke="var(--accent-orange)" stroke-width="1.4"/><path d="M1.5 3l4.5 3.5L10.5 3" fill="none" stroke="var(--accent-orange)" stroke-width="1.4"/></svg>
        <span>info@toolbaron.vegas</span>
      </div>
      <div class="contact-row">
        <svg viewBox="0 0 12 12" aria-hidden="true"><circle cx="6" cy="6" r="5" fill="none" stroke="var(--accent-orange)" stroke-width="1.3"/><ellipse cx="6" cy="6" rx="2.2" ry="5" fill="none" stroke="var(--accent-orange)" stroke-width="1"/><line x1="1" y1="6" x2="11" y2="6" stroke="var(--accent-orange)" stroke-width="1"/></svg>
        <span>www.toolbaron.vegas</span>
      </div>
    </div>
  </section>

</body>
</html>
```